MOSSGATE SPIRITWORKS WEBSITE

MOSSGATE SPIRITWORKS WHOLESALES ALCOHOL (WHISKY VODKA AND HELPS CREATES BOTTLING/BRANDING FOR PEOPLE WANTING LAUNCH THERE OWN BRANDS OF ALCOHOL

Colors

Designer to choose colors to be used in the design.

```html
<!DOCTYPE html>
<html lang="en">
<head>
<meta charset="utf-8">
<title>Mossgate Spiritworks</title>
<link rel="stylesheet" href="https://fonts.googleapis.com/css2?family=Michroma&family=Roboto:wght@400;500;700&display=swap">
<style>
:root{
  --gold:#f5b800;
  --gold-soft:#fdf9ec;
  --ink:#222222;
  --dark:#2b2a28;
  --grey:#8a8a8a;
  --line:#e6e6e6;
  --white:#ffffff;
}
*{box-sizing:border-box;margin:0;padding:0}
html,body{width:1200px;height:4532px;overflow:hidden}
body{position:relative;font-family:"Roboto",sans-serif;color:var(--ink);background:var(--white)}
.abs{position:absolute}
.section-title{position:absolute;left:0;width:1200px;text-align:center;font-family:"Michroma",sans-serif;font-size:38px;color:var(--ink);letter-spacing:1px}
.section-title::after{content:"";display:block;width:80px;height:3px;background:var(--gold);margin:8px auto 0}
.btn{position:absolute;display:flex;align-items:center;justify-content:center;background:var(--gold);color:var(--ink);font-weight:700;font-size:15px;text-transform:uppercase;clip-path:polygon(0 0,100% 0,calc(100% - 22px) 100%,0 100%);padding-right:22px}
.btn.dark{background:var(--dark);color:var(--white)}

/* top bar */
.topbar{position:absolute;left:0;top:0;width:1200px;height:42px;background:var(--dark);color:var(--white);font-size:13px}
.topbar .accent{position:absolute;right:0;top:0;width:338px;height:42px;background:var(--gold);clip-path:polygon(30px 0,100% 0,100% 100%,0 100%)}
.topbar .contact{position:absolute;left:111px;top:13px;display:flex;gap:14px;align-items:center}
.topbar .contact i{display:inline-block;width:10px;height:10px;background:var(--gold);border-radius:2px;margin-right:6px;vertical-align:-1px}
.social-dots{position:absolute;right:110px;top:14px;display:flex;gap:20px}
.social-dots span{width:12px;height:12px;border-radius:50%;background:rgba(43,42,40,.55)}

/* header */
.header{position:absolute;left:0;top:42px;width:1200px;height:94px;background:var(--white)}
.brand{position:absolute;left:111px;top:30px;display:flex;align-items:center;gap:10px;font-family:"Roboto",sans-serif;font-weight:700;font-size:22px;color:var(--ink);letter-spacing:1px}
.brand .mark{width:26px;height:26px;background:var(--gold)}
.nav{position:absolute;right:111px;top:38px;display:flex;font-size:14px;font-weight:700;text-transform:uppercase}
.nav a{padding:0 25px;border-left:1px solid var(--line);color:var(--ink);text-decoration:none}
.nav a:first-child{border-left:none;color:var(--gold)}
.nav a:last-child{padding-right:0}

/* hero */
.hero{position:absolute;left:0;top:136px;width:1200px;height:600px;overflow:hidden}
.hero .photo{position:absolute;inset:0;background:radial-gradient(ellipse at 72% 45%,#8a6a44 0%,#4a3420 40%,#1f160e 80%)}
.hero .shade{position:absolute;inset:0;background:linear-gradient(90deg,#1b1510 0%,#2a2016 100%);clip-path:polygon(0 0,700px 0,440px 600px,0 600px);opacity:.93}
.hero .eyebrow{position:absolute;left:111px;top:180px;font-family:"Michroma",sans-serif;font-size:20px;color:var(--white)}
.hero h1{position:absolute;left:111px;top:208px;font-family:"Michroma",sans-serif;font-weight:400;font-size:46px;color:var(--white);letter-spacing:1px}
.hero p{position:absolute;left:111px;top:276px;width:440px;font-size:22px;line-height:33px;color:var(--white)}
.dots{position:absolute;left:114px;top:564px;display:flex;gap:10px;align-items:center}
.dots span{width:9px;height:9px;border:1.5px solid var(--white);transform:rotate(45deg)}
.dots span.on{background:var(--white)}
.dots em{display:block;width:74px;height:1px;background:rgba(255,255,255,.6);margin-left:14px}

/* about */
.about-shot{position:absolute;border:6px solid var(--white);box-shadow:0 2px 8px rgba(0,0,0,.1)}
.about h2{position:absolute;left:686px;top:876px;font-family:"Michroma",sans-serif;font-weight:400;font-size:32px;padding-left:26px;border-left:3px solid var(--gold);line-height:32px}
.about p{position:absolute;left:686px;width:402px;font-size:13.5px;line-height:26px;color:var(--grey);text-align:justify}

/* wholesale */
.wholesale{position:absolute;left:0;top:1400px;width:1200px;height:756px;background:var(--gold-soft)}
.wholesale .lead{position:absolute;left:160px;top:140px;width:880px;text-align:center;font-size:14px;line-height:26px;color:#6b6b6b}
.tile{position:absolute;width:313px;height:213px;display:flex;align-items:center;justify-content:center;color:var(--white);font-weight:700;font-size:21px;text-transform:uppercase;text-shadow:0 1px 3px rgba(0,0,0,.5)}

/* services */
.card{position:absolute;width:308px;height:393px;background:var(--white);box-shadow:0 3px 14px rgba(0,0,0,.12);text-align:center}
.card .pic{position:absolute;left:5px;top:5px;width:298px;height:202px}
.card h3{position:absolute;left:0;top:232px;width:100%;font-size:16px;font-weight:700;text-transform:uppercase}
.card p{position:absolute;left:20px;top:275px;width:268px;font-size:13px;line-height:24px;color:var(--grey)}
.card a{position:absolute;left:0;top:352px;width:100%;font-size:13px;font-weight:700;color:var(--gold);text-decoration:underline}

/* contact */
.contact{position:absolute;left:0;top:2942px;width:1200px;height:537px;background:linear-gradient(180deg,#f3b600,#eeb000)}
.contact .section-title::after{background:var(--ink)}
.info-icon{position:absolute;width:62px;height:62px;border-radius:50%;background:var(--white);display:flex;align-items:center;justify-content:center}
.info-label{position:absolute;font-size:13px;font-weight:700;color:var(--ink);text-transform:uppercase}
.info-text{position:absolute;font-size:12.5px;line-height:19px;color:#5a4300}
.field{position:absolute;height:42px;background:var(--white);font-size:13px;color:var(--grey);padding:13px 16px}

/* faq */
.faq-item{position:absolute;left:213px;width:771px;background:var(--white);box-shadow:0 2px 10px rgba(0,0,0,.1);font-size:14px;font-weight:500}
.faq-item .q{position:absolute;left:20px;top:12px}
.faq-item .toggle{position:absolute;right:10px;top:5px;width:30px;height:30px;background:var(--gold);color:var(--ink);font-weight:700;font-size:22px;line-height:30px;text-align:center}
.faq-item .toggle.open{background:none;color:var(--gold)}
.faq-item .a{position:absolute;left:20px;top:50px;width:720px;font-size:13px;font-weight:400;line-height:22px;color:var(--grey)}

/* footer */
.footer{position:absolute;left:0;top:4174px;width:1200px;height:358px;background:var(--dark);color:var(--white)}
.footer h4{position:absolute;top:62px;font-size:16px;font-weight:700;text-transform:uppercase}
.footer ul{position:absolute;list-style:none;font-size:13px}
.footer li{height:39px;display:flex;align-items:flex-start;gap:22px}
.footer li::before{content:"»";color:var(--gold);font-weight:700}
.f-row{position:absolute;left:531px;width:220px;font-size:11.5px;line-height:17px}
.f-row b{display:block;font-size:13px;font-weight:700;margin-bottom:4px}
.f-row::before{content:"";position:absolute;left:-32px;top:2px;width:10px;height:10px;background:var(--gold);border-radius:50%}
.newsletter{position:absolute;left:804px;top:102px;width:283px;height:46px;background:var(--white);border:2px solid var(--gold)}
.newsletter span{position:absolute;left:16px;top:13px;font-size:13px;color:#555}
.newsletter b{position:absolute;right:0;top:0;width:106px;height:42px;background:var(--gold);color:var(--ink);font-size:13px;text-align:center;line-height:42px}
.f-social{position:absolute;top:174px;width:44px;height:44px;border-radius:50%;background:var(--white)}
.f-social.first{background:var(--gold)}
.footer .rule{position:absolute;left:111px;top:299px;width:976px;height:1px;background:rgba(255,255,255,.15)}
.footer .copy{position:absolute;left:0;top:318px;width:1200px;text-align:center;font-size:13px}
</style>
</head>
<body>

<div class="topbar">
  <div class="accent"></div>
  <div class="contact"><span><i></i>+31 20 555 0147</span><span>|</span><span><i></i>info@mossgatespirits.com</span></div>
  <div class="social-dots"><span></span><span></span><span></span><span></span></div>
</div>

<header class="header">
  <div class="brand"><span class="mark"></span>MOSSGATE SPIRITWORKS</div>
  <nav class="nav"><a>Home</a><a>About</a><a>Wholesale</a><a>Services</a><a>Contact</a></nav>
</header>

<section class="hero">
  <div class="photo" role="img" aria-label="Oak barrel with wine bottles and a filled glass on a rustic table"></div>
  <div class="shade"></div>
  <div class="eyebrow">WELCOME TO</div>
  <h1>MOSSGATE</h1>
  <p>Turn your next drink idea into a reality and share your product with the world.</p>
  <div class="btn" style="left:111px;top:367px;width:153px;height:50px">Learn More</div>
  <div class="dots"><span></span><span class="on"></span><span></span><span></span><em></em></div>
</section>

<section class="about">
  <div class="about-shot" style="left:303px;top:857px;width:323px;height:234px;background:linear-gradient(135deg,#b07a4a,#6a4024)" role="img" aria-label="Wine bottles resting in a wooden crate with straw"></div>
  <div class="about-shot" style="left:105px;top:971px;width:195px;height:209px;background:linear-gradient(160deg,#7a4a2a,#3a2414)" role="img" aria-label="Cellar shelves stocked with bottles"></div>
  <div class="about-shot" style="left:297px;top:1066px;width:279px;height:212px;background:linear-gradient(135deg,#d8d4cc,#8c9a7a)" role="img" aria-label="Labelled wine bottles lying in a box"></div>
  <h2>ABOUT US</h2>
  <p style="top:942px">Mossgate Spiritworks, located in the Netherlands, has been mixing creating 5-star-rated gin, cocktails and making recipes since 2017. Now we want to use our distilling expertise to help you launch your very own brand of liquor.</p>
  <p style="top:1058px">Through our vast network we have exclusive access some of the best Whiskies, Vodka, Rum, Gins and Wines in the world. We work directly with you to develop the perfect recipe and produce your drink.</p>
  <div class="btn" style="left:686px;top:1196px;width:154px;height:50px">Learn More</div>
</section>

<section class="wholesale">
  <div class="section-title" style="top:70px">WHOLESALE</div>
  <div class="lead">We have exclusive access to spirits from world-class distilleries globally producing award winning We are able to supply large volumes of high-end spirit world-wide if you wish to bottle in your own facility.</div>
  <div class="tile" style="left:111px;top:230px;background:linear-gradient(135deg,#1a1410,#7a4a1c)" role="img" aria-label="Whisky poured over ice">Whiskies</div>
  <div class="tile" style="left:443px;top:230px;background:linear-gradient(180deg,#1f4f9e,#0c1e44)" role="img" aria-label="Vodka shots on a blue lit bar">Vodka</div>
  <div class="tile" style="left:774px;top:230px;background:linear-gradient(135deg,#3c3a22,#8a7a44)" role="img" aria-label="Rum bottle on a coastal rock">Rum</div>
  <div class="tile" style="left:111px;top:465px;background:linear-gradient(135deg,#4a4e30,#8a8458)" role="img" aria-label="Gin bottle with herbs and citrus">Gins</div>
  <div class="tile" style="left:443px;top:465px;background:linear-gradient(135deg,#3a3424,#9a8a6a)" role="img" aria-label="Rows of wine bottles in a crate">Wines</div>
  <div class="tile" style="left:774px;top:465px;background:linear-gradient(135deg,#2a241e,#6a5440)" role="img" aria-label="Champagne bottle with cork">Champagnes</div>
</section>

<section class="services">
  <div class="section-title" style="top:2262px">SERVICES</div>
  <div class="card" style="left:111px;top:2349px">
    <div class="pic" style="background:linear-gradient(180deg,#2a1a10,#8a5a2c)" role="img" aria-label="Barrel cellar with rows of casks"></div>
    <h3>Recipe Development</h3>
    <p>Our team works with you to perfect your drink recipe to deliver the exact taste you're looking for.</p>
    <a>READ MORE</a>
  </div>
  <div class="card" style="left:445px;top:2349px">
    <div class="pic" style="background:linear-gradient(180deg,#4a4440,#c8b8a0)" role="img" aria-label="Hands sifting grain from a sack"></div>
    <h3>Trial Production</h3>
    <p>With your drink recipe ready, it's time to start production. We begin by producing a test batch of your drink</p>
    <a>READ MORE</a>
  </div>
  <div class="card" style="left:779px;top:2349px">
    <div class="pic" style="background:linear-gradient(180deg,#c89a6a,#d89a20)" role="img" aria-label="Rows of drink cans on a production line"></div>
    <h3>Canning Services</h3>
    <p>We now offer canning services for things like ready-made drinks in various sizes. You can ask our team about</p>
    <a>READ MORE</a>
  </div>
  <div class="btn" style="left:487px;top:2798px;width:222px;height:48px">View All Services</div>
</section>

<section class="contact">
  <div class="section-title" style="top:52px">CONTACT US</div>
  <div class="info-icon" style="left:191px;top:127px"><svg width="24" height="28" viewBox="0 0 24 28"><path d="M12 2a8 8 0 0 0-8 8c0 6 8 14 8 14s8-8 8-14a8 8 0 0 0-8-8z" fill="none" stroke="#222" stroke-width="2"/><circle cx="12" cy="10" r="3" fill="#222"/></svg></div>
  <div class="info-label" style="left:281px;top:128px">Location:</div>
  <div class="info-text" style="left:281px;top:148px;width:240px">Mossgate Spiritworks Building 14, Havenkade Noord, 3e Dwarsweg, Leiden, 2311XA</div>
  <div class="info-icon" style="left:560px;top:127px"><svg width="26" height="26" viewBox="0 0 24 24"><path d="M6 2l4 4-2 3c1 3 4 6 7 7l3-2 4 4-3 4C10 22 2 14 2 5z" fill="#222"/></svg></div>
  <div class="info-label" style="left:651px;top:138px">Phone:</div>
  <div class="info-text" style="left:651px;top:160px">+31 20 555 0147</div>
  <div class="info-icon" style="left:798px;top:127px"><svg width="26" height="20" viewBox="0 0 26 20"><rect x="1" y="1" width="24" height="18" fill="#222"/><path d="M1 1l12 10L25 1" fill="none" stroke="#fff" stroke-width="2"/></svg></div>
  <div class="info-label" style="left:885px;top:138px">Email:</div>
  <div class="info-text" style="left:885px;top:160px">info@mossgatespirits.com</div>

  <div class="field" style="left:165px;top:222px;width:282px">Full Name</div>
  <div class="field" style="left:457px;top:222px;width:282px">Last Name</div>
  <div class="field" style="left:751px;top:222px;width:282px">Company</div>
  <div class="field" style="left:165px;top:276px;width:282px">Email</div>
  <div class="field" style="left:457px;top:276px;width:282px">Telephone</div>
  <div class="field" style="left:751px;top:276px;width:282px">Website(Optional)</div>
  <div class="field" style="left:165px;top:332px;width:868px;height:86px">Message</div>
  <div class="btn dark" style="left:503px;top:433px;width:194px;height:49px">Send Message</div>
</section>

<section class="faq">
  <div class="section-title" style="top:3574px;font-size:26px">FREQUENTLY ASKED QUESTIONS</div>
  <div class="faq-item" style="top:3653px;height:40px"><span class="q">Where is Mossgate Spiritworks based?</span><span class="toggle">+</span></div>
  <div class="faq-item" style="top:3707px;height:40px"><span class="q">What if I am outside of the Netherlands? Can you still create my drink?</span><span class="toggle">+</span></div>
  <div class="faq-item" style="top:3762px;height:138px"><span class="q">Is it required to have experience in the beverage industry to make a drink?</span><span class="toggle open">–</span>
    <div class="a">There is no experience needed! You provide the idea, and our team provides the experts to help you launch your dream drink brand. We meet with you throughout the process to ensure that we help you create the highest-quality product.</div></div>
  <div class="faq-item" style="top:3913px;height:40px"><span class="q">What types of marketing and branding do you offer?</span><span class="toggle">+</span></div>
  <div class="faq-item" style="top:3970px;height:40px"><span class="q">Can your team help me meet the legal requirements for selling alcohol?</span><span class="toggle">+</span></div>
  <div class="faq-item" style="top:4026px;height:40px"><span class="q">What drinks can Mossgate Spiritworks help me create?</span><span class="toggle">+</span></div>
</section>

<footer class="footer">
  <div class="brand" style="left:111px;top:142px;color:var(--white);font-size:18px"><span class="mark"></span>MOSSGATE SPIRITWORKS</div>
  <h4 style="left:375px">Quick Links</h4>
  <ul style="left:378px;top:110px"><li>Home</li><li>About Us</li><li>Wholesale</li><li>Services</li><li>Contact</li></ul>
  <h4 style="left:531px">Contact Info</h4>
  <div class="f-row" style="left:564px;top:104px"><b>ADDRESS:</b>Mossgate Spiritworks Building 14, Havenkade Noord, 3e Dwarsweg, Leiden, 2311XA</div>
  <div class="f-row" style="left:564px;top:196px"><b>PHONE:</b>+31 20 555 0147</div>
  <div class="f-row" style="left:564px;top:252px;top:252px"><b>EMAIL:</b>info@mossgatespirits.com</div>
  <h4 style="left:804px">Newsletter Signup</h4>
  <div class="newsletter"><span>Email Address</span><b>SIGN UP</b></div>
  <div class="f-social first" style="left:805px"></div>
  <div class="f-social" style="left:856px"></div>
  <div class="f-social" style="left:907px"></div>
  <div class="f-social" style="left:958px"></div>
  <div class="rule"></div>
  <div class="copy">© 2022 <b>MOSSGATE SPIRITWORKS</b> &nbsp;|&nbsp; All Rights Reserved</div>
</footer>

</body>
</html>
```